New young doctors office business card

Doctor's office
Hello:
My name is Dr. Eduardo Maximino Ortega Benavides. I need a business card for my new office located within a hospital. The name of the hospital is "Hospital Almendral". Although the hospital logo and name must be included in the business card, please make me a personal logo for myself. The logo might be maybe my name in a stylish font, or my initials (EMOB) or something like that. Im more inclined to a font logo, rather than a image logo, but a good one might change my mind. The info on my business card is going to be in spanish. The following info must be included please (the info within parenthesis is not to be included, it is provided for you to understand it since it's in spanish, so you can properly place it on the card):
-Dr. Eduardo Maximino Ortega Benavides (my name)
-Medicina general (My specialty)
-Hospital Almendral (The name of the hospital where my office is)
-Calle Tomás Ocampo #247 Col. Almendral (address)
-Tel 471-5836 (Office phone)
-Sábado y domingo 10:00 am a 10:00pm (Office hours)
-Emergencias: 555-917-4402 (Emergency phone)
-maximinoob@correoficticio.mx (email)
-English Spoken
So, that's all the info i need to be on the business card. Although it's a business card for a doctor's office, i dont want it to be a boring, plain business card. Make it eye-catchy and stylish please. As i said, the hospital logo must be included. You'll find it on the heading of the PDF file i attached, but dont make it the center of attention.
Physician
Hello:My name is Dr. Eduardo Maximino Ortega Benavides. I need a business card for my new office located within a hospital. The name of the hospital is "Hospital Almendral". Although the hospital logo and name must be included in the business card, please make me a personal logo for myself. The logo might be maybe my name in a stylish font, or my initials (EMOB) or something like that. Im more inclined to a font logo, rather than a image logo, but a good one might change my mind. The info on my business card is going to be in spanish. The following info must be included please (the info within parenthesis is not to be included, it is provided for you to understand it since it's in spanish, so you can properly place it on the card):-Dr. Eduardo Maximino Ortega Benavides (my name)-Medicina general (My specialty)-Hospital Almendral (The name of the hospital where my office is)-Calle Tomás Ocampo #247 Col. Almendral (address)-Tel 471-5836 (Office phone)-Sábado y domingo 10:00 am a 10:00pm (Office hours)-Emergencias: 555-917-4402 (Emergency phone)-maximinoob@correoficticio.mx (email)-English Spoken So, that's all the info i need to be on the business card. Although it's a business card for a doctor's office, i dont want it to be a boring, plain business card. Make it eye-catchy and stylish please. As i said, the hospital logo must be included. You'll find it on the heading of the PDF file i attached, but dont make it the center of attention.

```html
<!DOCTYPE html>
<html lang="es">
<head>
<meta charset="utf-8">
<title>Tarjeta de presentación — Dr. Eduardo Maximino Ortega Benavides</title>
<link rel="stylesheet" href="https://fonts.googleapis.com/css2?family=Fira+Sans:ital,wght@0,400;0,600;0,700;1,400&display=swap">
<style>
  :root {
    --brand-blue: #263f8c;
    --ink: #2b2b2f;
    --muted: #55565c;
    --bubble: #cfd0d3;
    --paper: #ffffff;
    --backdrop: #e6e7ea;
  }
  * { box-sizing: border-box; margin: 0; padding: 0; }
  html, body {
    width: 1200px; height: 900px; overflow: hidden;
    background: var(--backdrop);
    font-family: "Fira Sans", Arial, sans-serif;
  }
  .sheet {
    width: 1200px; height: 900px;
    display: flex; align-items: center; justify-content: center; gap: 40px;
  }
  .card {
    position: relative;
    width: 540px; height: 309px;
    background: var(--paper);
    box-shadow: 0 6px 18px rgba(0,0,0,.15);
    overflow: hidden;
  }

  /* Front */
  .doctor-name {
    position: absolute; left: 150px; top: 28px;
    font-size: 17px; font-weight: 700; color: var(--brand-blue);
    letter-spacing: .1px; white-space: nowrap;
  }
  .specialty {
    position: absolute; left: 150px; top: 50px;
    font-size: 12.5px; font-style: italic; color: var(--ink);
  }
  .contact-list {
    position: absolute; left: 150px; top: 80px;
    list-style: none; font-size: 12.5px; color: var(--ink); line-height: 20px;
  }
  .contact-list li { display: flex; align-items: center; gap: 8px; white-space: nowrap; }
  .contact-list svg { width: 12px; height: 12px; fill: var(--brand-blue); flex: none; }
  .hospital-mark {
    position: absolute; left: 44px; top: 160px;
    width: 40px; height: 40px; background: var(--brand-blue);
  }
  .hospital-block {
    position: absolute; left: 100px; top: 156px;
    font-size: 13px; line-height: 17px; color: var(--muted); font-style: normal;
  }
  .hospital-name { color: var(--brand-blue); font-size: 14px; }
  .english-bubble {
    position: absolute; left: 410px; top: 166px;
    width: 96px; height: 46px;
  }
  .english-bubble svg { position: absolute; inset: 0; }
  .bubble-text {
    position: absolute; left: 0; right: 0; top: 8px;
    display: flex; flex-direction: column; align-items: center;
    font-size: 10.5px; font-weight: 600; letter-spacing: .8px;
    color: var(--ink); line-height: 12px;
  }
  .monogram {
    position: absolute; right: 30px; bottom: 22px;
    font-size: 60px; font-weight: 700; color: var(--brand-blue);
    letter-spacing: 2px; line-height: 1;
  }

  /* Back */
  .card-back svg { display: block; }
  .back-letters {
    font-family: "Fira Sans", Arial, sans-serif;
    font-weight: 700; font-size: 200px;
  }
</style>
</head>
<body>
<main class="sheet">

  <section class="card card-front" aria-label="Frente de la tarjeta">
    <h1 class="doctor-name">Dr. Eduardo Maximino Ortega Benavides</h1>
    <p class="specialty">Medicina general</p>
    <ul class="contact-list">
      <li>
        <svg viewBox="0 0 24 24" aria-hidden="true"><path d="M6.6 10.8a15.2 15.2 0 0 0 6.6 6.6l2.2-2.2a1 1 0 0 1 1-.25 11.4 11.4 0 0 0 3.6.57 1 1 0 0 1 1 1V20a1 1 0 0 1-1 1A17 17 0 0 1 3 4a1 1 0 0 1 1-1h3.5a1 1 0 0 1 1 1c0 1.25.2 2.45.57 3.6a1 1 0 0 1-.25 1z"/></svg>
        Tel 471-5836 | Emergencias: 555-917-4402
      </li>
      <li>
        <svg viewBox="0 0 24 24" aria-hidden="true"><path d="M2 5h20L12 12.5zM2 7.2v11.8h20V7.2l-10 7.5z"/></svg>
        maximinoob@correoficticio.mx
      </li>
      <li>
        <svg viewBox="0 0 24 24" aria-hidden="true"><path d="M12 2a10 10 0 1 0 0 20 10 10 0 0 0 0-20zm0 3a7 7 0 1 1 0 14 7 7 0 0 1 0-14zm-1 2v6l5 3 1-1.6-4-2.4V7z"/></svg>
        Sábado y domingo 10:00 am a 10:00 pm
      </li>
    </ul>

    <div class="hospital-mark" aria-hidden="true"></div>
    <address class="hospital-block">
      <div class="hospital-name">Hospital Almendral</div>
      <div>Calle Tomás Ocampo #247</div>
      <div>Col. Almendral</div>
    </address>

    <div class="english-bubble">
      <svg viewBox="0 0 96 46" aria-hidden="true">
        <ellipse cx="48" cy="20" rx="46" ry="19" fill="#cfd0d3"/>
        <path d="M22 32 L12 45 L32 36 Z" fill="#cfd0d3"/>
      </svg>
      <p class="bubble-text"><span>ENGLISH</span><span>SPOKEN</span></p>
    </div>

    <div class="monogram">EMOB</div>
  </section>

  <section class="card card-back" aria-label="Reverso de la tarjeta">
    <svg width="540" height="309" viewBox="0 0 540 309">
      <defs>
        <clipPath id="band-area"><rect x="0" y="150" width="540" height="130"/></clipPath>
        <clipPath id="paper-area">
          <rect x="0" y="0" width="540" height="150"/>
          <rect x="0" y="280" width="540" height="29"/>
        </clipPath>
      </defs>
      <rect width="540" height="309" fill="#ffffff"/>
      <rect class="accent-band" x="0" y="150" width="540" height="130" fill="#263f8c"/>
      <g clip-path="url(#paper-area)">
        <text class="back-letters" x="20" y="226" textLength="500" lengthAdjust="spacingAndGlyphs" fill="#263f8c">EMOB</text>
      </g>
      <g clip-path="url(#band-area)">
        <text class="back-letters" x="20" y="226" textLength="500" lengthAdjust="spacingAndGlyphs" fill="#ffffff">EMOB</text>
      </g>
    </svg>
  </section>

</main>
</body>
</html>
```